website for 'thebrightnook' which is a specialise tutoring company for children with learning difficu

We need a website for a new business that is focused on assessment and then specialised tutoring for young children with learning difficulties. The website needs to be simple but fun and fresh. We have an existing logo (uploaded) that needs to be the building block for the website. The website doesn't need to be overly content-heavy.

Target Market(s)

parents

Industry/Entity Type

Education

Number of Pages Required

3 page

Font styles to use
Other font styles liked:
• possibly matched to the logo

Requirements
Must have
• a initial front page which introduces the business and provides contact details, a second page that will allow for a more content-heavy section, a third page which focuses on introducing the staff (initially 3 staff ),

```html
<!DOCTYPE html>
<html lang="en">
<head>
<meta charset="utf-8">
<title>The Bright Nook – Specialised Learning for Children</title>
<link rel="stylesheet" href="https://fonts.googleapis.com/css2?family=Lato:wght@400;700&family=Bitter:wght@400&family=Kaushan+Script&display=swap">
<style>
:root{
  --green:#8dc63f;
  --green-light:#a6d35f;
  --dark:#1d1d1d;
  --dark-band:rgba(28,28,28,.88);
  --text:#222;
  --white:#fff;
  --muted:#9a9a9a;
}
*{box-sizing:border-box;margin:0;padding:0}
html,body{width:849px;height:1200px;overflow:hidden;background:var(--white)}
body{font-family:"Lato",sans-serif;color:var(--text)}
.page{position:relative;width:849px;height:1200px;overflow:hidden}
.abs{position:absolute}

/* hero */
.hero-photo{left:0;top:0;width:849px;height:460px;
  background:linear-gradient(180deg,#5a3a34 0%,#8a6a5c 30%,#c9b6a4 60%,#a79284 100%)}
.hero-caption{left:0;top:391px;width:849px;height:70px;background:var(--dark-band)}
.hero-caption p{position:absolute;left:61px;top:20px;font-family:"Bitter",serif;font-size:17.5px;color:var(--white);letter-spacing:.1px}
.hero-wave{left:0;top:445px}

.nav{left:62px;top:34px;display:flex;gap:22px;font-weight:700;font-size:14px;color:var(--white)}
.nav .active{color:var(--green)}
.nav-mark{left:78px;top:13px;width:10px;height:10px;border-radius:50%;background:var(--white)}

.logo-badge{left:341px;top:-44px;width:166px;height:166px;border-radius:50%;background:var(--white);
  display:flex;flex-direction:column;align-items:center;justify-content:center;padding-top:44px}
.logo-dot{width:22px;height:22px;border-radius:50%;background:var(--green);margin-bottom:6px}
.logo-name{font-family:"Lato",sans-serif;font-size:21px;font-weight:400;color:#3a3a3a}
.logo-tag{font-size:7px;color:#777;letter-spacing:.6px;margin-top:2px}

.header-phone{left:624px;top:29px;display:flex;align-items:center;gap:10px;color:var(--white);font-weight:700;font-size:17.5px}
.icon-circle{width:30px;height:30px;border-radius:50%;background:var(--green);display:flex;align-items:center;justify-content:center}

/* intro */
.script-title{font-family:"Kaushan Script",cursive;font-size:25px;color:var(--dark)}
.script-title em{font-style:normal;color:var(--green)}
.welcome-title{left:61px;top:490px;display:flex;align-items:center;gap:8px}
.tick-dot{width:18px;height:18px;border-radius:50%;background:var(--green)}
.welcome-text{left:61px;top:531px;width:420px;font-size:10.6px;line-height:17px;color:var(--text)}
.btn{display:flex;align-items:center;background:var(--dark);color:var(--white);border-radius:2px;overflow:hidden;font-weight:700}
.btn .btn-cap{width:32px;height:100%;background:var(--green);border-radius:0 50% 50% 0}
.btn-info{left:60px;top:664px;width:136px;height:32px;font-size:13.5px;font-weight:400}
.btn-info span{margin-left:10px}

.video-title{left:514px;top:488px}
.video-frame{left:513px;top:530px;width:277px;height:166px;
  background:linear-gradient(135deg,#6f8a5a 0%,#b9a38a 45%,#8c6e58 100%)}
.video-play{left:122px;top:68px;width:31px;height:31px;border-radius:50%;background:var(--white)}
.video-bar{left:0;bottom:0;width:277px;height:27px;background:#111}
.video-track{left:42px;top:12px;width:224px;height:3px;background:#777}
.video-progress{left:42px;top:12px;width:78px;height:3px;background:#d01818}

/* contact */
.contact-band{left:0;top:725px;width:849px;height:323px}
.contact-title{left:277px;top:803px}
.contact-text{left:276px;top:845px;width:515px;font-size:10.4px;line-height:14px;color:var(--dark)}
.field{background:var(--white);font-size:10.2px;color:#333;padding:0 8px;display:flex;align-items:center;border:1px solid #d8e8c4}
.f-name{left:276px;top:880px;width:248px;height:32px}
.f-email{left:529px;top:880px;width:260px;height:32px}
.f-phone{left:276px;top:918px;width:248px;height:32px}
.f-service{left:529px;top:918px;width:260px;height:32px;justify-content:space-between}
.f-msg{left:276px;top:957px;width:248px;height:59px;align-items:flex-start;padding-top:8px}
.btn-submit{left:529px;top:959px;width:104px;height:32px;font-size:15px;letter-spacing:.5px}
.btn-submit span{margin-left:10px}

/* footer */
.footer{left:0;top:1047px;width:849px;height:153px;background:var(--dark)}
.footer-item{position:absolute;top:25px;display:flex;gap:10px}
.footer-item .icon-circle{width:33px;height:33px}
.footer-label{font-size:10px;color:var(--green);font-weight:700;margin-top:2px}
.footer-strong{font-size:11.5px;color:var(--white);font-weight:700;margin-top:2px}
.footer-big{font-size:15px;color:var(--white);font-weight:700;margin-top:3px}
.footer-small{font-size:9.6px;color:#ccc;line-height:15px;margin-top:1px}
.fi-loc{left:96px}.fi-call{left:341px}.fi-mail{left:545px}
.footer-rule{position:absolute;left:60px;top:105px;width:730px;height:1px;background:#3a3a3a}
.copyright{position:absolute;left:61px;top:124px;font-size:9.8px;color:var(--muted)}
.social{position:absolute;right:59px;top:115px;display:flex;gap:8px}
.social span{width:25px;height:25px;border-radius:50%;border:2px solid #ccc}
.s1{background:#3b5998}.s2{background:#0e76a8}.s3{background:#2aa9e0}.s4{background:#d93c2b}
</style>
</head>
<body>
<div class="page">

  <div class="abs hero-photo" role="img" aria-label="Photo of two parents helping a boy and a girl with schoolwork at a table"></div>
  <div class="abs hero-caption"><p>We Are A Specialized Tutoring Company For Children Suffering With Learning Difficulties</p></div>
  <svg class="abs hero-wave" width="849" height="20" viewBox="0 0 849 20">
    <path d="M0 0 H849 V14 C760 20 700 10 600 14 C480 19 380 8 260 13 C160 17 80 9 0 12 Z" fill="rgba(28,28,28,.88)"/>
  </svg>

  <div class="abs nav-mark"></div>
  <nav class="abs nav"><span class="active">Home</span><span>Services</span><span>Our Staff</span></nav>

  <div class="abs logo-badge">
    <div class="logo-dot"></div>
    <div class="logo-name">thebrightnook</div>
    <div class="logo-tag">specialised learning for children</div>
  </div>

  <div class="abs header-phone">
    <div class="icon-circle">
      <svg width="14" height="14" viewBox="0 0 24 24"><path fill="#1d1d1d" d="M6.6 10.8a15 15 0 0 0 6.6 6.6l2.2-2.2c.3-.3.7-.4 1-.2 1.1.4 2.3.6 3.6.6.6 0 1 .4 1 1V20c0 .6-.4 1-1 1A17 17 0 0 1 3 4c0-.6.4-1 1-1h3.5c.6 0 1 .4 1 1 0 1.3.2 2.5.6 3.6.1.3 0 .7-.2 1z"/></svg>
    </div>
    <span>123 - 456 - 7890</span>
  </div>

  <div class="abs welcome-title"><div class="tick-dot"></div><h2 class="script-title">Welcome to <em>The Bright Nook</em></h2></div>
  <p class="abs welcome-text">Lorem ipsum dolor sit amet, consectetuer adipiscing elit, sed diam nonummy nibhk euismod tincidunt ut laoreet dolore magna aliquam erat volutpat. Ut wisi enim admi minim veniam, quis nostrud exerci tation ullamcorper suscipit lobortis nisl ut aliquip ex ea commodo consequat. Duis autem vel eum iriure dolor in hendrerit in vulputat te velit esse molestie consequat, vel illum dolore eu feugiat nulla facilisis at veromi eros et accumsan et iusto odio dignissim qui blandit praesent luptatum zzril delenit augue duis dolore te feugait nulla facilisi.</p>
  <div class="abs btn btn-info"><div class="btn-cap"></div><span>Get More Info</span></div>

  <h2 class="abs script-title video-title">View <em>Our Video</em></h2>
  <div class="abs video-frame" role="img" aria-label="Video still of a tutor working with a young girl at a desk">
    <div class="abs video-play">
      <svg width="31" height="31" viewBox="0 0 31 31"><path d="M13 10 L21 15.5 L13 21 Z" fill="#111"/></svg>
    </div>
    <div class="abs video-bar">
      <svg class="abs" style="left:9px;top:8px" width="24" height="12" viewBox="0 0 24 12"><path d="M0 0 L7 6 L0 12 Z" fill="#fff"/><rect x="14" y="0" width="3" height="12" fill="#fff"/><rect x="20" y="0" width="3" height="12" fill="#fff"/></svg>
      <div class="abs video-track"></div>
      <div class="abs video-progress"></div>
    </div>
  </div>

  <svg class="abs contact-band" width="849" height="323" viewBox="0 0 849 323">
    <path d="M0 10 C120 2 200 14 330 8 C470 2 560 14 690 9 C770 6 810 10 849 8 V323 H0 Z" fill="#8dc63f"/>
  </svg>
  <h2 class="abs script-title contact-title">Quick Contact</h2>
  <p class="abs contact-text">Duis autem vel eum iriure dolor in hendrerit in vulputat te velit esse molestie consequat, vel illum dolore eu feugiat nulla facilisis at veromi eros et accumsan et iusto odio</p>
  <div class="abs field f-name">Enter Your Name</div>
  <div class="abs field f-email">Enter Your Email</div>
  <div class="abs field f-phone">Enter Your Phone</div>
  <div class="abs field f-service"><span>Select Services</span>
    <svg width="9" height="6" viewBox="0 0 9 6"><path d="M1 1 L4.5 4.5 L8 1" stroke="#111" stroke-width="1.6" fill="none"/></svg></div>
  <div class="abs field f-msg">Messages</div>
  <div class="abs btn btn-submit"><div class="btn-cap"></div><span>SUBMIT</span></div>

  <footer class="abs footer">
    <div class="footer-item fi-loc">
      <div class="icon-circle"><svg width="14" height="18" viewBox="0 0 14 18"><path d="M7 0a7 7 0 0 0-7 7c0 5 7 11 7 11s7-6 7-11a7 7 0 0 0-7-7zm0 10a3 3 0 1 1 0-6 3 3 0 0 1 0 6z" fill="#1d1d1d"/></svg></div>
      <div><div class="footer-label">Our Location</div><div class="footer-strong">The Bright Nook</div><div class="footer-small">16 Lorem ipsum dolor sit amet,&nbsp; Sed<br>benetion, Street no-123456</div></div>
    </div>
    <div class="footer-item fi-call">
      <div class="icon-circle"><svg width="15" height="15" viewBox="0 0 24 24"><path fill="#1d1d1d" d="M6.6 10.8a15 15 0 0 0 6.6 6.6l2.2-2.2c.3-.3.7-.4 1-.2 1.1.4 2.3.6 3.6.6.6 0 1 .4 1 1V20c0 .6-.4 1-1 1A17 17 0 0 1 3 4c0-.6.4-1 1-1h3.5c.6 0 1 .4 1 1 0 1.3.2 2.5.6 3.6.1.3 0 .7-.2 1z"/></svg></div>
      <div><div class="footer-label">Call Us Today</div><div class="footer-big">123 - 456 - 7890</div></div>
    </div>
    <div class="footer-item fi-mail">
      <div class="icon-circle"><svg width="18" height="13" viewBox="0 0 18 13"><rect x="1" y="1" width="16" height="11" fill="none" stroke="#1d1d1d" stroke-width="1.6"/><path d="M1 1 L9 7 L17 1" fill="none" stroke="#1d1d1d" stroke-width="1.6"/></svg></div>
      <div><div class="footer-label">Email Us Today</div><div class="footer-big">info@thebrightnook.com</div></div>
    </div>
    <div class="footer-rule"></div>
    <p class="copyright">Copyright © 2016 The Bright Nook. All Rights Reserved.</p>
    <div class="social"><span class="s1"></span><span class="s2"></span><span class="s3"></span><span class="s4"></span></div>
  </footer>

</div>
</body>
</html>
```